Create a basic website for a new air cargo consultancy, called 'Zephyrra Logistics'

We want to build a basic website (homepage, 'about us' page, services and contact us page).
We have a logo, we have most of the text to be inserted, but not all. We also still need to take pictures.
We would like to have a fresh and modern, but business like design and the creation of the website.
We want to be able to modify the website after (add pictures and more text, update references).
We already have a url.

```html
<!DOCTYPE html>
<html lang="en">
<head>
<meta charset="utf-8">
<title>Zephyrra Logistics</title>
<link href="https://fonts.googleapis.com/css2?family=Montserrat:wght@400;500;600;700&display=swap" rel="stylesheet">
<style>
:root{
  --blue:#2b3597;
  --blue-light:#4652ad;
  --gold:#d9a02a;
  --ink:#222;
  --muted:#666;
  --form-bg:#e5e5e5;
  --white:#fff;
  --black:#050505;
}
*{box-sizing:border-box;margin:0;padding:0}
html,body{width:1200px;height:3629px;overflow:hidden}
body{position:relative;font-family:'Montserrat',sans-serif;color:var(--ink);background:var(--white)}
.abs{position:absolute}
.btn{position:absolute;display:flex;align-items:center;justify-content:center;background:var(--gold);color:var(--white);font-weight:600;border-radius:30px;text-transform:uppercase}
.photo{position:absolute;border-radius:50%}
.ring{position:absolute;border-radius:50%;border:1.5px dashed var(--gold)}

/* hero */
.hero{position:absolute;left:0;top:0;width:1200px;height:671px;background:var(--blue);overflow:hidden}
.hero-disc{position:absolute;left:620px;top:-120px;width:1000px;height:1000px;border-radius:50%;background:var(--blue-light)}
.brand{position:absolute;left:34px;top:40px;color:var(--gold);font-weight:600;font-size:26px;display:flex;align-items:center;gap:10px}
.brand-dot{width:14px;height:14px;border-radius:50%;background:var(--gold)}
.nav a{position:absolute;top:53px;color:var(--white);font-size:15px;font-weight:500;text-decoration:none}
.hero-title{left:64px;top:250px;color:var(--white);font-size:58px;font-weight:600}
.hero-sub{left:64px;top:343px;width:500px;color:#e6e8f5;font-size:16px;line-height:20px}
.hero-rings .ring{border-color:rgba(217,160,42,.8)}
.hero-photo{position:absolute;left:730px;top:190px;width:450px;height:481px;background:linear-gradient(180deg,#5460b4,#3a3f7a 60%,#2d2a3a);border-radius:200px 200px 0 0}

/* about */
.about-title{left:620px;top:926px;color:var(--blue);font-size:38px;font-weight:600}
.about-text{left:618px;top:1005px;width:520px;font-size:16px;line-height:30px;color:var(--muted)}
.stat{position:absolute;top:1400px;display:flex;align-items:center;gap:14px}
.stat-num{font-size:74px;font-weight:600;color:var(--blue);line-height:72px}
.stat-label{font-size:18px;color:#333;margin-left:4px}
.divider{position:absolute;top:1370px;width:1px;height:185px;background:#eee}

/* services */
.services{position:absolute;left:0;top:1655px;width:1200px;height:785px;background:linear-gradient(180deg,#2b3597,#3440a0)}
.services-title{left:145px;top:1776px;color:var(--white);font-size:38px;font-weight:600}
.svc{position:absolute;top:1912px;width:330px;text-align:center;color:var(--white)}
.svc h3{margin-top:300px;font-size:21px;font-weight:600}
.svc p{margin:20px auto 0;width:300px;font-size:12px;line-height:19px;color:#dde0f2}
.svc .more{margin-top:18px;display:flex;justify-content:center;align-items:center;gap:10px;color:var(--gold);font-size:11px;font-weight:600}
.arrow-c{width:26px;height:26px;border-radius:50%;border:1.5px solid currentColor;display:flex;align-items:center;justify-content:center}

/* contact */
.contact{position:absolute;left:0;top:2440px;width:1200px;height:577px;background:linear-gradient(180deg,#fafafa,#eef0f2)}
.contact-title{left:660px;top:2560px;color:var(--blue);font-size:38px;font-weight:600}
.c-item{position:absolute;left:92px;display:flex;align-items:center;gap:22px;font-size:20px;font-weight:500;color:#333}
.c-icon{width:56px;height:56px;border-radius:50%;border:1.5px solid var(--gold);display:flex;align-items:center;justify-content:center;background:var(--white)}
.form{position:absolute;left:560px;top:2655px;width:550px;height:463px;background:var(--form-bg);z-index:2}
.field{position:absolute;background:#f6f6f6;border:1px solid #fff;font-size:13px;color:#888;padding:16px 20px}

/* footer */
.footer{position:absolute;left:0;top:3017px;width:1200px;height:612px;background:var(--black);color:var(--white)}
.f-logo{position:absolute;left:67px;top:3218px;width:280px;height:112px;background:var(--white);border-bottom:4px solid var(--blue);display:flex;align-items:center;justify-content:center;gap:10px;color:var(--gold);font-size:22px;font-weight:600}
.f-desc{left:67px;top:3363px;width:320px;font-size:12px;line-height:15px;color:#888}
.f-head{top:3222px;color:var(--gold);font-size:22px;font-weight:600}
.f-link{position:absolute;display:flex;align-items:center;gap:12px;font-size:14px;color:var(--white)}
.f-link .arrow-c{color:var(--gold);width:26px;height:26px}
.f-link span{color:var(--white)}
.f-email{position:absolute;left:905px;top:3292px;width:235px;height:51px;border-radius:26px;background:var(--white);color:#555;font-size:14px;padding:16px 25px}
.f-rule{left:64px;top:3545px;width:1086px;height:1px;background:#333}
.f-copy{left:0;top:3580px;width:1200px;text-align:center;font-size:16px;color:#ddd}
</style>
</head>
<body>

<header class="hero">
  <div class="hero-disc"></div>
  <div class="brand"><span class="brand-dot"></span>Zephyrra</div>
  <nav class="nav">
    <a style="left:271px">HOME</a>
    <a style="left:402px">ABOUT</a>
    <a style="left:544px">SERVICES</a>
    <a style="left:704px">BLOG</a>
    <a style="left:823px">CONTACT</a>
  </nav>
  <div class="btn" style="left:995px;top:42px;width:142px;height:40px;font-size:13px">Get Started</div>
  <div class="hero-rings">
    <div class="ring" style="left:688px;top:138px;width:492px;height:492px"></div>
    <div class="ring" style="left:730px;top:178px;width:410px;height:410px"></div>
  </div>
  <div class="hero-photo" role="img" aria-label="Photo of two business consultants reviewing a tablet"></div>
  <h1 class="abs hero-title">Zephyrra Logistics</h1>
  <p class="abs hero-sub">Welcome to Zephyrra Logistics, your premier consultancy specialized in the air cargo sector.</p>
  <div class="btn" style="left:64px;top:416px;width:201px;height:55px;font-size:19px">Get Started</div>
</header>

<section class="about">
  <div class="ring" style="left:84px;top:830px;width:484px;height:484px"></div>
  <div class="photo" role="img" aria-label="Photo of two colleagues walking through an airport terminal" style="left:114px;top:862px;width:428px;height:428px;background:radial-gradient(circle at 50% 35%,#c9cdd6,#6d7280 70%,#3c3f48)"></div>
  <h2 class="abs about-title">About Us</h2>
  <p class="abs about-text">Welcome to Zephyrra Logistics, your premier consultancy specialized in the air cargo sector. We are dedicated to helping clients enhance their overall cargo strategy, drive digital transformation, fostercommunity building, and achieve sustainability goals.</p>
  <div class="btn" style="left:618px;top:1187px;width:187px;height:54px;font-size:19px">Read More</div>

  <div class="stat" style="left:120px">
    <svg width="100" height="100" viewBox="0 0 100 100" fill="none" stroke="#2b3597" stroke-width="3"><path d="M30 20h36v18a18 18 0 0 1-36 0z"/><path d="M30 26H18a12 12 0 0 0 12 14M66 26h12a12 12 0 0 1-12 14"/><path d="M48 56v12M36 80h24l-4-12H40z"/><path d="M82 60l2 6 6 2-6 2-2 6-2-6-6-2 6-2z"/></svg>
    <div><div class="stat-num">98%</div><div class="stat-label">Consulting Success</div></div>
  </div>
  <div class="divider" style="left:440px"></div>
  <div class="stat" style="left:466px">
    <svg width="100" height="100" viewBox="0 0 100 100" fill="none" stroke="#2b3597" stroke-width="3"><circle cx="34" cy="22" r="7"/><circle cx="50" cy="20" r="7"/><circle cx="66" cy="22" r="7"/><path d="M10 50l18-10 22 14 22-14 18 10-10 26-30 12-30-12z"/><path d="M36 64l10 10M46 58l14 14"/></svg>
    <div><div class="stat-num">120+</div><div class="stat-label">Worldwide Client</div></div>
  </div>
  <div class="divider" style="left:782px"></div>
  <div class="stat" style="left:826px">
    <svg width="100" height="100" viewBox="0 0 100 100" fill="none" stroke="#2b3597" stroke-width="3"><circle cx="50" cy="50" r="22"/><circle cx="50" cy="50" r="14"/><path d="M43 50l5 5 9-10"/><path d="M36 68l-8 20 10-4 6 8 6-18M64 68l8 20-10-4-6 8-6-18"/><path d="M50 8l3 7 7 1-5 5 1 7-6-3-6 3 1-7-5-5 7-1z"/></svg>
    <div><div class="stat-num">20+</div><div class="stat-label">Years Of Experience</div></div>
  </div>
</section>

<section class="services">
  <div role="img" aria-label="Faint photo of a cargo aircraft in the background" style="position:absolute;left:0;top:160px;width:1200px;height:560px;background:radial-gradient(ellipse at 60% 60%,rgba(120,130,200,.25),transparent 70%)"></div>
</section>
<h2 class="abs services-title">Our Services</h2>
<div class="btn" style="left:880px;top:1776px;width:186px;height:54px;font-size:19px">View More</div>

<div class="ring" style="left:148px;top:1912px;width:270px;height:270px;border-color:rgba(217,160,42,.7)"></div>
<div class="photo" role="img" aria-label="Photo of a team in a planning meeting" style="left:165px;top:1929px;width:236px;height:236px;background:radial-gradient(circle at 50% 40%,#e4c7c0,#8c6a5c 70%,#4a3a34)"></div>
<div class="ring" style="left:473px;top:1912px;width:270px;height:270px;border-color:rgba(217,160,42,.7)"></div>
<div class="photo" role="img" aria-label="Photo of a woman working on a laptop" style="left:490px;top:1929px;width:236px;height:236px;background:radial-gradient(circle at 50% 40%,#f0d4b8,#c04a3f 70%,#7a3530)"></div>
<div class="ring" style="left:800px;top:1912px;width:270px;height:270px;border-color:rgba(217,160,42,.7)"></div>
<div class="photo" role="img" aria-label="Photo of a group of young people gathered around a laptop" style="left:817px;top:1929px;width:236px;height:236px;background:radial-gradient(circle at 50% 40%,#c8c0b4,#7a5a4c 70%,#3c3230)"></div>

<div class="svc" style="left:118px"><h3>Strategic Planning</h3><p>We help you navigate the complexities of the global cargo landscape, ensuring your business stays competitive and resilient.</p><div class="more">VIEW MORE <span class="arrow-c">→</span></div></div>
<div class="svc" style="left:443px"><h3>Digitalization</h3><p>We help you navigate the complexities of the global cargo landscape, ensuring your business stays competitive and resilient.</p><div class="more">VIEW MORE <span class="arrow-c">→</span></div></div>
<div class="svc" style="left:787px"><h3>Community Building</h3><p>We help you navigate the complexities of the global cargo landscape, ensuring your business stays competitive and resilient.</p><div class="more">VIEW MORE <span class="arrow-c">→</span></div></div>

<section class="contact"></section>
<h2 class="abs contact-title">Contact Us</h2>
<div class="c-item" style="top:2657px"><span class="c-icon"><svg width="26" height="26" viewBox="0 0 24 24" fill="#d9a02a"><path d="M6.6 10.8a15 15 0 0 0 6.6 6.6l2.2-2.2a1 1 0 0 1 1-.25 11.4 11.4 0 0 0 3.6.57 1 1 0 0 1 1 1V20a1 1 0 0 1-1 1A17 17 0 0 1 3 4a1 1 0 0 1 1-1h3.5a1 1 0 0 1 1 1c0 1.25.2 2.45.57 3.6a1 1 0 0 1-.25 1z"/></svg></span>(+62)500 274 918</div>
<div class="c-item" style="top:2757px"><span class="c-icon"><svg width="28" height="28" viewBox="0 0 24 24" fill="#d9a02a"><path d="M3 9l9-6 9 6v11H3z"/><path d="M3 9l9 6 9-6" stroke="#fff" stroke-width="1.5" fill="none"/></svg></span>hello@zephyrra-mail.com</div>
<div class="c-item" style="top:2864px"><span class="c-icon"><svg width="24" height="28" viewBox="0 0 24 28" fill="#d9a02a"><path d="M12 0a10 10 0 0 0-10 10c0 7 10 18 10 18s10-11 10-18A10 10 0 0 0 12 0zm0 14a4 4 0 1 1 0-8 4 4 0 0 1 0 8z"/></svg></span>Jl. Angin Baru No.12, Kuta</div>

<div class="form">
  <div class="field" style="left:43px;top:67px;width:212px;height:51px">Name</div>
  <div class="field" style="left:290px;top:67px;width:213px;height:51px">Email</div>
  <div class="field" style="left:43px;top:136px;width:212px;height:51px">Phone</div>
  <div class="field" style="left:290px;top:136px;width:213px;height:51px">Subject</div>
  <div class="field" style="left:45px;top:210px;width:458px;height:130px">Message</div>
  <div class="btn" style="left:185px;top:377px;width:193px;height:55px;font-size:19px">Send Now</div>
</div>

<footer class="footer"></footer>
<div class="f-logo"><span class="brand-dot"></span>Zephyrra Logistics</div>
<p class="abs f-desc">Welcome to Zephyrra Logistics, your premier consultancy specialized in the air cargo sector.</p>

<h4 class="abs f-head" style="left:446px">Company</h4>
<div class="f-link" style="left:444px;top:3278px"><span class="arrow-c">→</span><span>HOME</span></div>
<div class="f-link" style="left:444px;top:3329px"><span class="arrow-c">→</span><span>ABOUT</span></div>
<div class="f-link" style="left:444px;top:3374px"><span class="arrow-c">→</span><span>SERVICES</span></div>
<div class="f-link" style="left:444px;top:3421px"><span class="arrow-c">→</span><span>BLOG</span></div>
<div class="f-link" style="left:444px;top:3470px"><span class="arrow-c">→</span><span>CONTACT</span></div>

<h4 class="abs f-head" style="left:668px">Quick Links</h4>
<div class="f-link" style="left:668px;top:3278px"><span class="arrow-c">→</span><span>FAQS</span></div>
<div class="f-link" style="left:668px;top:3326px"><span class="arrow-c">→</span><span>Privacy Policy</span></div>
<div class="f-link" style="left:668px;top:3374px"><span class="arrow-c">→</span><span>Cookies Policy</span></div>
<div class="f-link" style="left:668px;top:3423px"><span class="arrow-c">→</span><span>Term &amp; Conditions</span></div>

<h4 class="abs f-head" style="left:895px">Get Latest Updates</h4>
<div class="f-email">Email Address</div>
<div class="btn" style="left:905px;top:3364px;width:235px;height:51px;font-size:17px">Subscribe Now</div>

<div class="abs f-rule"></div>
<p class="abs f-copy">Privacy Policy | © Copyright 2024, All Rights Reserved.</p>

</body>
</html>
```